Re-brand our business and design!

We need a simple informational website (editable for in the future use)
We need our logo(we have included logo), name, who we are, and what we do displayed.

This is our current site (which is not acceptable, and only a template site): all our information is on this site, please use it forreferanceofinformation.
Www.brightlanefixers.com

Target Market(s)

Real estate brokers, and realtors,homeowners, and anyone looking for home repairs.

Industry/Entity Type

Business

Number of Pages Required

4 page

Font styles to use
Sans Serif

Requirements
Must have
• Our name, contact info, services, and our logo (which we will Email upon request)
• MUST have originality to the site.
• custom "contact us form" or request an estimate form.
Nice to have
• page for real customer testimonies.
• page for our previous work where we can upload pics of completed jobs.
Should not have
• any infringements on any copyrights or plagiarism at all.

```html
<!DOCTYPE html>
<html lang="en">
<head>
<meta charset="utf-8">
<title>Bright Lane Fixers And Maintenance</title>
<link href="https://fonts.googleapis.com/css2?family=Roboto:wght@300;400;500;700&family=Lato:wght@400;700&display=swap" rel="stylesheet">
<style>
:root{
  --red:#e0161b;
  --black:#0b0b0b;
  --dark:#1c1c1c;
  --light:#eeeeee;
  --grey:#8a8a8a;
  --text:#444;
  --white:#fff;
}
*{margin:0;padding:0;box-sizing:border-box}
html,body{width:1200px;height:3629px;overflow:hidden;background:var(--white)}
body{font-family:'Roboto',sans-serif;color:var(--text)}
.page{position:relative;width:1200px;height:3629px;overflow:hidden}
.abs{position:absolute}

/* header */
.site-header{left:0;top:0;width:1200px;height:135px;background:var(--black)}
.brand{left:80px;top:0;width:215px;height:174px;background:var(--white);display:flex;flex-direction:column;align-items:center;justify-content:center;z-index:3;text-align:center}
.brand-name{font-weight:700;font-size:19px;color:var(--dark);line-height:1.25}
.brand-mark{width:16px;height:16px;background:var(--red);margin-bottom:10px}
.call{right:80px;top:16px;display:flex;align-items:center;gap:14px}
.call-text{font-size:14px;color:var(--white);line-height:1.2}
.call-text strong{display:block;font-size:29px;font-weight:500;color:var(--red)}
.main-nav{right:80px;top:95px;display:flex;align-items:center}
.main-nav a{color:var(--white);font-size:15px;text-decoration:none;padding:0 23px;position:relative}
.main-nav a.active{color:var(--red)}
.main-nav .search{padding-left:18px}

/* hero */
.hero{left:0;top:135px;width:1200px;height:552px;
  background:
   radial-gradient(ellipse 260px 330px at 300px 300px,rgba(60,80,120,.55),transparent 70%),
   radial-gradient(ellipse 200px 180px at 280px 470px,rgba(150,100,50,.6),transparent 70%),
   radial-gradient(ellipse 340px 300px at 930px 170px,rgba(255,246,225,.9),transparent 70%),
   linear-gradient(90deg,#5b4a3c 0%,#8a6e55 30%,#c9a57a 60%,#f1dfc0 85%,#e8d2ac 100%)}
.hero-title{right:80px;top:325px;font-family:'Lato',sans-serif;font-weight:700;font-size:62px;color:var(--black);letter-spacing:-.5px}
.hero-sub{right:80px;top:408px;font-size:24px;color:var(--dark)}
.hero-btn{right:80px;top:452px;width:260px;height:62px;background:var(--red);color:var(--white);font-size:20px;display:flex;align-items:center;justify-content:center}
.slide-arrow{top:362px;width:50px;height:50px;border:2px solid rgba(255,255,255,.8);border-radius:50%;background:rgba(0,0,0,.25)}

/* welcome */
.welcome{left:0;top:687px;width:1200px;height:390px;text-align:center}
.welcome-kicker{position:absolute;left:0;right:0;top:62px;font-size:20px;color:var(--black)}
.welcome-title{position:absolute;left:0;right:0;top:88px;font-size:46px;font-weight:400;color:var(--red)}
.welcome-text{position:absolute;left:100px;right:100px;top:155px;font-size:14.5px;line-height:26px;color:var(--grey)}
.btn{position:absolute;left:514px;top:268px;width:172px;height:58px;background:var(--red);color:var(--white);font-size:18px;display:flex;align-items:center;justify-content:center}

/* services */
.service{position:absolute;left:0;width:1200px;height:313px;background:var(--light)}
.service .photo{position:absolute;left:0;top:0}
.service-body{position:absolute;top:46px;width:430px}
.service-body.right{left:733px}
.service-body.left{left:78px}
.service-icon{display:block;width:64px;height:64px}
.service-title{margin-top:18px;font-size:31px;font-weight:400;color:var(--red)}
.service-list{margin-top:6px;font-size:15px;line-height:27px;color:var(--text);list-style:none}

/* testimonials */
.testimonials{left:0;top:2955px;width:1200px;height:385px;text-align:center}
.testi-title{position:absolute;left:0;right:0;top:55px;font-size:42px;font-weight:400;color:var(--red)}
.quote-mark{position:absolute;left:568px;top:122px;width:64px;height:64px;border:2px solid var(--red);border-radius:50%;color:var(--red);font-size:40px;font-family:'Lato',sans-serif;font-weight:700;line-height:60px}
.testi-text{position:absolute;left:240px;right:240px;top:207px;font-size:15px;line-height:28px;color:var(--grey)}
.client{position:absolute;left:0;right:0;top:275px;font-size:16px;color:var(--red)}
.client em{font-size:14px}
.dots{position:absolute;left:572px;top:312px;display:flex;gap:12px}
.dots span{width:11px;height:11px;border-radius:50%;background:var(--red)}

/* footer */
.site-footer{left:0;top:3340px;width:1200px;height:230px;background:#111}
.f-col{position:absolute;top:26px}
.f-col h4{font-size:17px;font-weight:700;color:#6e1012;margin-bottom:14px;letter-spacing:.3px}
.f-col p,.f-col li{font-size:14px;line-height:22px;color:#bbb;list-style:none}
.f-col li{line-height:32px}
.f-col li.active{color:var(--red)}
.f-contact p{display:flex;gap:10px;margin-bottom:10px}
.f-contact .ic{width:14px;height:14px;border:1.5px solid var(--red);border-radius:2px;flex:none;margin-top:4px}
.f-input{width:250px;height:52px;border:1px solid #888;color:#ccc;font-size:15px;padding:15px 16px;margin-top:6px}
.f-btn{width:250px;height:52px;background:var(--red);color:var(--white);font-size:20px;display:flex;align-items:center;justify-content:center;margin-top:20px}
.copyright{left:0;top:3570px;width:1200px;height:59px;background:var(--red);color:var(--white);font-size:15px;display:flex;align-items:center;justify-content:center}
</style>
</head>
<body>
<div class="page">

  <header class="abs site-header">
    <div class="abs brand">
      <span class="brand-mark"></span>
      <span class="brand-name">Bright Lane Fixers<br>And Maintenance</span>
    </div>
    <div class="abs call">
      <svg width="48" height="48" viewBox="0 0 24 24"><path fill="#e0161b" d="M6.6 10.8c1.4 2.8 3.8 5.1 6.6 6.6l2.2-2.2c.3-.3.7-.4 1-.2 1.1.4 2.3.6 3.6.6.6 0 1 .4 1 1V20c0 .6-.4 1-1 1C10.6 21 3 13.4 3 4c0-.6.4-1 1-1h3.5c.6 0 1 .4 1 1 0 1.3.2 2.5.6 3.6.1.3 0 .7-.2 1l-2.3 2.2z"/></svg>
      <div class="call-text">Call Us Now<strong>555-014-2290</strong></div>
    </div>
    <nav class="abs main-nav">
      <a class="active" href="#">HOME
        <svg class="abs" style="left:20px;top:-28px" width="50" height="22" viewBox="0 0 50 22"><path d="M2 20 L25 3 L48 20" fill="none" stroke="#e0161b" stroke-width="3"/></svg>
      </a>
      <a href="#">ABOUT US</a>
      <a href="#">SERVICES</a>
      <a href="#">CONTACT US</a>
      <a class="search" href="#"><svg width="24" height="24" viewBox="0 0 24 24"><circle cx="10" cy="10" r="7" fill="none" stroke="#e0161b" stroke-width="3"/><path d="M15 15l6 6" stroke="#e0161b" stroke-width="3.5" stroke-linecap="round"/></svg></a>
    </nav>
  </header>

  <section class="abs hero" role="img" aria-label="Handyman wearing a tool belt and work gloves in a sunlit room with wooden floor"></section>
  <div class="abs slide-arrow" style="left:12px"><svg width="46" height="46" viewBox="0 0 46 46"><path d="M26 15l-8 8 8 8" fill="none" stroke="#fff" stroke-width="2.5"/></svg></div>
  <div class="abs slide-arrow" style="right:12px"><svg width="46" height="46" viewBox="0 0 46 46"><path d="M20 15l8 8-8 8" fill="none" stroke="#fff" stroke-width="2.5"/></svg></div>
  <h1 class="abs hero-title">Home Repair Services</h1>
  <p class="abs hero-sub">Serving the Maple Ridge, and surrounding areas</p>
  <a class="abs hero-btn">CONTACT US KNOW</a>

  <section class="abs welcome">
    <p class="welcome-kicker">WELCOME TO</p>
    <h2 class="welcome-title">BRIGHT LANE FIXERS AND MAINTENANCE</h2>
    <p class="welcome-text">Lorem Ipsum is simply dummy text of the printing and typesetting industry. Lorem Ipsum has been the industry's standard dummy text ever since the 1500s, when an unknown printer took a galley of type and scrambled it to make a type specimen book. It has survived not only five centuries, but also the leap into electronic typesetting, remaining essentially unchanged. It was popularised in the 1960s with the release of Letraset sheets containing Lorem Ipsum passages, and more recently with desktop publishing software like</p>
    <a class="btn">KNOW MORE</a>
  </section>

  <!-- Carpentry -->
  <section class="service" style="top:1077px">
    <svg class="photo" width="1200" height="313" role="img" aria-label="Carpenter planing a wooden board">
      <defs>
        <linearGradient id="g1" x1="0" x2="1"><stop offset="0" stop-color="#4a3a2c"/><stop offset=".5" stop-color="#2a221c"/><stop offset="1" stop-color="#5a4838"/></linearGradient>
        <radialGradient id="h1" cx=".45" cy=".55" r=".45"><stop offset="0" stop-color="#b08a62" stop-opacity=".7"/><stop offset="1" stop-color="#b08a62" stop-opacity="0"/></radialGradient>
        <radialGradient id="s1" cx=".1" cy=".85" r=".35"><stop offset="0" stop-color="#c8b090" stop-opacity=".55"/><stop offset="1" stop-color="#c8b090" stop-opacity="0"/></radialGradient>
      </defs>
      <polygon points="0,0 600,0 700,156 600,313 0,313" fill="url(#g1)"/>
      <polygon points="0,0 600,0 700,156 600,313 0,313" fill="url(#h1)"/>
      <polygon points="0,0 600,0 700,156 600,313 0,313" fill="url(#s1)"/>
      <polyline points="600,0 700,156 600,313" fill="none" stroke="#e0161b" stroke-width="3"/>
    </svg>
    <div class="service-body right">
      <svg class="service-icon" viewBox="0 0 64 64" aria-hidden="true">
        <path d="M14 50 L40 24" stroke="#0b0b0b" stroke-width="6" stroke-linecap="round"/>
        <path d="M32 12 L48 8 L56 16 L52 20 L46 16 L42 20 L36 16 Z" fill="#0b0b0b"/>
        <rect x="8" y="52" width="48" height="6" fill="#0b0b0b"/>
      </svg>
      <h3 class="service-title">CARPENTRY</h3>
      <ul class="service-list"><li>Stairs, Floors, Decks, Fences</li><li>Storage sheds, Storage shelving and doors</li><li>Vapor barrier repair/installation, Attic and crawl space,</li></ul>
    </div>
  </section>

  <!-- Plumbing -->
  <section class="service" style="top:1390px">
    <svg class="photo" width="1200" height="313" role="img" aria-label="Chrome faucet and pipes">
      <defs>
        <linearGradient id="g2" x1="0" x2="1"><stop offset="0" stop-color="#1e2630"/><stop offset="1" stop-color="#4c5864"/></linearGradient>
        <radialGradient id="h2" cx=".55" cy=".4" r=".4"><stop offset="0" stop-color="#c9d3dc" stop-opacity=".55"/><stop offset="1" stop-color="#c9d3dc" stop-opacity="0"/></radialGradient>
        <radialGradient id="s2" cx=".85" cy=".6" r=".3"><stop offset="0" stop-color="#a8b4c0" stop-opacity=".45"/><stop offset="1" stop-color="#a8b4c0" stop-opacity="0"/></radialGradient>
      </defs>
      <polygon points="600,0 1200,0 1200,313 600,313 500,156" fill="url(#g2)"/>
      <polygon points="600,0 1200,0 1200,313 600,313 500,156" fill="url(#h2)"/>
      <polygon points="600,0 1200,0 1200,313 600,313 500,156" fill="url(#s2)"/>
      <polyline points="600,0 500,156 600,313" fill="none" stroke="#e0161b" stroke-width="3"/>
    </svg>
    <div class="service-body left">
      <svg class="service-icon" viewBox="0 0 64 64" aria-hidden="true">
        <path d="M44 8a12 12 0 0 0-11 16L10 47a5 5 0 0 0 7 7l23-23a12 12 0 0 0 16-11l-8 4-6-4 0-7 8-5z" fill="#0b0b0b"/>
      </svg>
      <h3 class="service-title">PLUMBING</h3>
      <ul class="service-list"><li>Bathrooms, Kitchens, Washer/Dryer Hook Up</li><li>Clogged drains, Toilets, Tubs/Showers</li><li>Sinks, Garbage disposals, Leaking faucets vent repair</li></ul>
    </div>
  </section>

  <!-- Doors & windows -->
  <section class="service" style="top:1703px">
    <svg class="photo" width="1200" height="313" role="img" aria-label="House front with window and arched wooden door">
      <defs>
        <linearGradient id="g3" x1="0" x2="1"><stop offset="0" stop-color="#34382a"/><stop offset=".4" stop-color="#6a6250"/><stop offset="1" stop-color="#5a4636"/></linearGradient>
        <radialGradient id="h3" cx=".3" cy=".3" r=".3"><stop offset="0" stop-color="#d8d0c0" stop-opacity=".5"/><stop offset="1" stop-color="#d8d0c0" stop-opacity="0"/></radialGradient>
        <radialGradient id="s3" cx=".8" cy=".65" r=".3"><stop offset="0" stop-color="#3a2418" stop-opacity=".7"/><stop offset="1" stop-color="#3a2418" stop-opacity="0"/></radialGradient>
      </defs>
      <polygon points="0,0 600,0 700,156 600,313 0,313" fill="url(#g3)"/>
      <polygon points="0,0 600,0 700,156 600,313 0,313" fill="url(#h3)"/>
      <polygon points="0,0 600,0 700,156 600,313 0,313" fill="url(#s3)"/>
      <polyline points="600,0 700,156 600,313" fill="none" stroke="#e0161b" stroke-width="3"/>
    </svg>
    <div class="service-body right">
      <svg class="service-icon" viewBox="0 0 64 64" aria-hidden="true">
        <rect x="6" y="6" width="52" height="52" fill="none" stroke="#0b0b0b" stroke-width="4"/>
        <path d="M10 10 L24 16 L24 54 L10 54 Z M54 10 L40 16 L40 54 L54 54 Z" fill="#0b0b0b"/>
      </svg>
      <h3 class="service-title">DOORS &amp; WINDOWS</h3>
      <ul class="service-list"><li>Weatherstripping, Replacements</li><li>Glass and Screen Installation and Repair, Install</li><li>locksets</li></ul>
    </div>
  </section>

  <!-- Electrical -->
  <section class="service" style="top:2016px">
    <svg class="photo" width="1200" height="313" role="img" aria-label="Electrician testing colored wires with a multimeter">
      <defs>
        <linearGradient id="g4" x1="0" x2="1"><stop offset="0" stop-color="#2e2420"/><stop offset="1" stop-color="#3c3a30"/></linearGradient>
        <radialGradient id="h4" cx=".8" cy=".2" r=".4"><stop offset="0" stop-color="#8a9a40" stop-opacity=".55"/><stop offset="1" stop-color="#8a9a40" stop-opacity="0"/></radialGradient>
        <radialGradient id="s4" cx=".4" cy=".65" r=".35"><stop offset="0" stop-color="#a07860" stop-opacity=".55"/><stop offset="1" stop-color="#a07860" stop-opacity="0"/></radialGradient>
      </defs>
      <polygon points="600,0 1200,0 1200,313 600,313 500,156" fill="url(#g4)"/>
      <polygon points="600,0 1200,0 1200,313 600,313 500,156" fill="url(#h4)"/>
      <polygon points="600,0 1200,0 1200,313 600,313 500,156" fill="url(#s4)"/>
      <polyline points="600,0 500,156 600,313" fill="none" stroke="#e0161b" stroke-width="3"/>
    </svg>
    <div class="service-body left">
      <svg class="service-icon" viewBox="0 0 64 64" aria-hidden="true">
        <circle cx="32" cy="32" r="30" fill="#0b0b0b"/>
        <rect x="22" y="12" width="5" height="12" fill="#fff"/>
        <rect x="37" y="12" width="5" height="12" fill="#fff"/>
        <path d="M17 24 H47 V32 a15 15 0 0 1-30 0 Z" fill="#fff"/>
        <rect x="29" y="44" width="6" height="10" fill="#fff"/>
      </svg>
      <h3 class="service-title">ELECTRICAL</h3>
      <ul class="service-list"><li>Bright Lane Fixers has licensed electricians who</li><li>can rewire your entire house, or just a GFCI. We can</li><li>respond to your electrical needs quickly.Code/Service.</li></ul>
    </div>
  </section>

  <!-- Roofing -->
  <section class="service" style="top:2329px">
    <svg class="photo" width="1200" height="313" role="img" aria-label="Roofer working on shingles with a hammer">
      <defs>
        <linearGradient id="g5" x1="0" x2="1"><stop offset="0" stop-color="#1f1c1c"/><stop offset="1" stop-color="#4e4240"/></linearGradient>
        <radialGradient id="h5" cx=".6" cy=".4" r=".45"><stop offset="0" stop-color="#8a7268" stop-opacity=".55"/><stop offset="1" stop-color="#8a7268" stop-opacity="0"/></radialGradient>
        <radialGradient id="s5" cx=".15" cy=".3" r=".3"><stop offset="0" stop-color="#0a0a0a" stop-opacity=".7"/><stop offset="1" stop-color="#0a0a0a" stop-opacity="0"/></radialGradient>
      </defs>
      <polygon points="0,0 600,0 700,156 600,313 0,313" fill="url(#g5)"/>
      <polygon points="0,0 600,0 700,156 600,313 0,313" fill="url(#h5)"/>
      <polygon points="0,0 600,0 700,156 600,313 0,313" fill="url(#s5)"/>
      <polyline points="600,0 700,156 600,313" fill="none" stroke="#e0161b" stroke-width="3"/>
    </svg>
    <div class="service-body right">
      <svg class="service-icon" viewBox="0 0 64 64" aria-hidden="true">
        <path d="M4 34 L32 10 L60 34 L54 34 L32 16 L10 34 Z" fill="#0b0b0b"/>
        <path d="M14 34 L32 20 L50 34 V56 H14 Z" fill="#0b0b0b"/>
        <rect x="27" y="40" width="10" height="16" fill="#fff"/>
      </svg>
      <h3 class="service-title">ROOFING MAINTENANCE</h3>
      <ul class="service-list"><li>Painting, Pressure/Power washing Heavy lifting,</li><li>Property Clean Outs Minor Repairs Vinyl Siding,</li><li>Gutters, Clean and seal tile, Caulking, Patch and repair.</li></ul>
    </div>
  </section>

  <!-- Small construction -->
  <section class="service" style="top:2642px">
    <svg class="photo" width="1200" height="313" role="img" aria-label="Builders in hard hats reviewing plans inside a timber frame">
      <defs>
        <linearGradient id="g6" x1="0" x2="1"><stop offset="0" stop-color="#3a2c20"/><stop offset="1" stop-color="#7a6044"/></linearGradient>
        <radialGradient id="h6" cx=".75" cy=".3" r=".3"><stop offset="0" stop-color="#e8c050" stop-opacity=".55"/><stop offset="1" stop-color="#e8c050" stop-opacity="0"/></radialGradient>
        <radialGradient id="s6" cx=".4" cy=".7" r=".35"><stop offset="0" stop-color="#c8b898" stop-opacity=".45"/><stop offset="1" stop-color="#c8b898" stop-opacity="0"/></radialGradient>
      </defs>
      <polygon points="600,0 1200,0 1200,313 600,313 500,156" fill="url(#g6)"/>
      <polygon points="600,0 1200,0 1200,313 600,313 500,156" fill="url(#h6)"/>
      <polygon points="600,0 1200,0 1200,313 600,313 500,156" fill="url(#s6)"/>
      <polyline points="600,0 500,156 600,313" fill="none" stroke="#e0161b" stroke-width="3"/>
    </svg>
    <div class="service-body left">
      <svg class="service-icon" viewBox="0 0 64 64" aria-hidden="true">
        <path d="M10 40 a22 22 0 0 1 44 0 Z" fill="#0b0b0b"/>
        <rect x="29" y="14" width="6" height="14" fill="#fff"/>
        <rect x="4" y="40" width="56" height="7" rx="2" fill="#0b0b0b"/>
      </svg>
      <h3 class="service-title">SMALL CONSTRUCTION</h3>
      <ul class="service-list"><li>Stairs, Floors, Decks, Fences</li><li>Storage sheds, Storage shelves Masonry</li></ul>
    </div>
  </section>

  <section class="abs testimonials">
    <h2 class="testi-title">WHAT OUR CLIENT SAY</h2>
    <div class="quote-mark">&laquo;</div>
    <p class="testi-text">"Lorem Ipsum is simply dummy text of the printing and typesetting industry. Lorem Ipsum has been the industry's standard dummy text ever since an unknown printer took a galley."</p>
    <p class="client">CLIENT NAME, ( <em>Lorem Ipsum</em> )</p>
    <div class="dots"><span></span><span></span><span></span></div>
  </section>

  <footer class="abs site-footer">
    <div class="f-col" style="left:80px;width:210px">
      <h4>ABOUT US</h4>
      <p>" Lorem Ipsum is simply dummy text of the printing and type setting of the industry Lorem Ipsum nknown as the printer took a galley of . . ."</p>
    </div>
    <div class="f-col" style="left:355px">
      <h4>USEFULL LINK</h4>
      <ul><li class="active">Home</li><li>About Us</li><li>Services</li><li>Contact Us</li></ul>
    </div>
    <div class="f-col f-contact" style="left:610px;width:240px">
      <h4>CONTACT INFO</h4>
      <p><span class="ic"></span><span>Bright Lane Fixers And Maintenance<br>Address citystate pincode office</span></p>
      <p><span style="width:14px"></span><span>555-014-2290</span></p>
      <p><span class="ic"></span><span>owen@brightlanefixers.com</span></p>
    </div>
    <div class="f-col" style="left:872px">
      <h4>NEWS LETTER</h4>
      <div class="f-input">Email*</div>
      <div class="f-btn">SUBSCRIBE</div>
    </div>
  </footer>
  <div class="abs copyright">© Bright Lane Fixers And Maintenance 2016 All rights reserved.</div>

</div>
</body>
</html>
```